World first health care product in tablet form to help save relationships and marriages

The product known as Venquara is in tablet form 470mg and has 30 to a packet the packet size is approx 11cm in length x 4cm We want to use the color of the image attached for the package and cornflower blue for our name Venquara. We also need to mention close to our name....... maintaining relationships with increased libido and desire ...... Our tablets are in a tamper-proof blister pack inserted into the package. We do not have a logo as yet, we are thinking of ven in small white letters and then QUARA in large letters in cornflower blue or something a bit darker. (The O could also contain a smiley face) We are not that fussed with a logo as yet, maybe down the track if our product works and sells. As of today business in Australia has ground to a halt with this coronavirus and its as bad as you could imagine. Please help us make this new product work with a fabulous packet design.
Target Market(s)
females and males
Industry/Entity Type
Pharmaceutical
Requirements
Must have
- the colors of the images attached and cornflower blue

```html
<!DOCTYPE html>
<html lang="en">
<head>
<meta charset="utf-8">
<title>Venquara – Tablet Pack</title>
<link rel="stylesheet" href="https://fonts.googleapis.com/css2?family=Montserrat:wght@600&family=Quicksand:wght@400&display=swap">
<style>
  :root {
    --page-bg: #ffffff;
    --pack-teal: #33b8a3;
    --pack-text: #ffffff;
    --name-accent: #3a5663;
  }
  * { margin: 0; padding: 0; box-sizing: border-box; }
  html, body {
    width: 1200px;
    height: 1000px;
    overflow: hidden;
    background: var(--page-bg);
  }
  .canvas {
    position: relative;
    width: 1200px;
    height: 1000px;
  }
  .pack-face {
    position: absolute;
    left: 35px;
    top: 295px;
    width: 1130px;
    height: 410px;
    background: var(--pack-teal);
  }
  .pack-spec {
    position: absolute;
    right: 12px;
    top: 15px;
    font-family: "Quicksand", sans-serif;
    font-weight: 400;
    font-size: 23px;
    letter-spacing: 2.6px;
    color: var(--pack-text);
    white-space: nowrap;
  }
  .pack-spec .dot {
    display: inline-block;
    width: 7px;
    height: 7px;
    margin: 0 18px 4px 16px;
    border-radius: 50%;
    background: var(--pack-text);
    vertical-align: middle;
  }
  .product-name {
    position: absolute;
    left: 0;
    right: 0;
    top: 164px;
    text-align: center;
    font-family: "Montserrat", sans-serif;
    font-weight: 600;
    font-size: 130px;
    line-height: 1;
    letter-spacing: 4px;
    white-space: nowrap;
  }
  .product-name .name-lead { color: var(--pack-text); }
  .product-name .name-accent { color: var(--name-accent); }
  .tagline {
    position: absolute;
    left: 0;
    right: 0;
    top: 352px;
    text-align: center;
    font-family: "Quicksand", sans-serif;
    font-weight: 400;
    font-size: 24px;
    letter-spacing: 3.8px;
    color: var(--pack-text);
    white-space: nowrap;
  }
</style>
</head>
<body>
  <main class="canvas">
    <section class="pack-face" aria-label="Venquara tablet pack front">
      <p class="pack-spec">470mg<span class="dot"></span>30 Tablets</p>
      <h1 class="product-name"><span class="name-lead">VEN</span><span class="name-accent">QUARA</span></h1>
      <p class="tagline">maintaining relationships with increased libido and desire</p>
    </section>
  </main>
</body>
</html>
```